Darrow Consulting needs a quality & professional business card!

I am a recruitment and employment consultant from Brisbane, Australia and I had a fantastic logo organised by this community to I am hoping the business card will be the same.

I have attached the Darrow consulting logo that ideally would feature on the back of the business card. There are a number of logos for you to use as you see fit. I would like the colour cheme to match that of the Darrow Consulting logo. I also have a secondary company called Career Lantern Australia and I have included that logo as well. While it is an important part of the business I don't want this logo feature too predominantly as I am moving out of this space. This logo was created by myself and is of low quality. Feel free to use the icon and words however you want. The winning design will be smart, professional and eye-catching.

The information I am looking for in the business card is:
Name: Gavin Darrow
Position: Founder & Director
Phone: (07) 3519 6482
Mobile: 0431 586 207
Email: gavin@careerlantern.com.au

Target Market(s)

Recruiters, government, large companies

Contact Information for Business Card

Name: Gavin Darrow
Phone: (07) 3519 6482
Mobile: 0431 586 207
Web: www.careerlantern.com.au

Font styles to use
Serif
Sans Serif

Requirements
Must have
• Darrow Consulting Logo on reverse side
• Contact details on front side with smaller reference to Darrow Consulting logo and Career Lantern Australia logo

```html
<!DOCTYPE html>
<html lang="en">
<head>
<meta charset="utf-8">
<title>Darrow Consulting – Business Card</title>
<link href="https://fonts.googleapis.com/css2?family=Montserrat:wght@400;500;600;700&display=swap" rel="stylesheet">
<style>
  :root {
    --backdrop: #0c0c0d;
    --card: #161719;
    --card-edge: #222326;
    --ink: #e4e5e7;
    --ink-muted: #8c8e92;
    --accent-blue: #1e8fd8;
  }
  * { box-sizing: border-box; margin: 0; padding: 0; }
  html, body {
    width: 1200px; height: 711px; overflow: hidden;
    background: var(--backdrop);
    font-family: "Montserrat", sans-serif;
    color: var(--ink);
  }
  .canvas {
    position: relative; width: 1200px; height: 711px;
    display: flex; align-items: center; justify-content: center; gap: 50px;
  }
  .card {
    position: relative; width: 520px; height: 297px;
    background: var(--card);
    border: 1px solid var(--card-edge);
    border-radius: 3px;
  }

  /* Brand name placeholder: one colour, one weight */
  .brand {
    display: flex; align-items: center;
    font-weight: 600; color: var(--ink); white-space: nowrap;
  }
  .brand__square { flex: none; background: var(--ink); }

  /* Front side */
  .brand--small {
    position: absolute; top: 40px; right: 40px;
    gap: 10px; font-size: 16px;
  }
  .brand--small .brand__square { width: 18px; height: 18px; }

  .partner {
    position: absolute; top: 120px; right: 40px;
    display: flex; align-items: center; gap: 8px;
    font-size: 11px; font-weight: 600; color: var(--ink);
  }
  .partner__dot {
    width: 18px; height: 18px; border-radius: 50%; background: var(--ink);
  }

  .person {
    position: absolute; left: 40px; top: 150px;
  }
  .person__name {
    font-size: 15px; font-weight: 700; letter-spacing: 0.03em; color: var(--ink);
  }
  .person__role {
    font-size: 11px; font-weight: 500; letter-spacing: 0.02em; color: var(--accent-blue);
    margin-top: 2px;
  }
  .person__rule {
    width: 44px; height: 1px; background: var(--accent-blue); margin-top: 5px;
  }
  .contacts {
    position: absolute; left: 40px; top: 214px;
    list-style: none; display: flex; flex-direction: column; gap: 9px;
  }
  .contacts__item {
    display: flex; align-items: center; gap: 12px;
    font-size: 11px; font-weight: 500; color: var(--ink);
  }
  .contacts__icon { width: 12px; height: 12px; flex: none; }
  .contacts__email { text-transform: uppercase; }

  /* Back side */
  .card--back { display: flex; align-items: center; justify-content: center; }
  .brand--large { gap: 16px; font-size: 34px; }
  .brand--large .brand__square { width: 36px; height: 36px; }
</style>
</head>
<body>
<main class="canvas">

  <section class="card card--front" aria-label="Business card front">
    <div class="brand brand--small">
      <span class="brand__square"></span>
      <span class="brand__name">Darrow Consulting</span>
    </div>

    <div class="partner">
      <span class="partner__dot"></span>
      <span class="partner__name">Career Lantern Australia</span>
    </div>

    <div class="person">
      <div class="person__name">GAVIN DARROW</div>
      <div class="person__role">FOUNDER &amp; DIRECTOR</div>
      <div class="person__rule"></div>
    </div>

    <ul class="contacts">
      <li class="contacts__item">
        <svg class="contacts__icon" viewBox="0 0 24 24" aria-hidden="true">
          <path fill="#1e8fd8" d="M6.6 10.8a15.1 15.1 0 0 0 6.6 6.6l2.2-2.2a1 1 0 0 1 1-.25 11.4 11.4 0 0 0 3.6.57 1 1 0 0 1 1 1V20a1 1 0 0 1-1 1A17 17 0 0 1 3 4a1 1 0 0 1 1-1h3.5a1 1 0 0 1 1 1c0 1.25.2 2.45.57 3.57a1 1 0 0 1-.25 1z"/>
        </svg>
        (07) 3519 6482
      </li>
      <li class="contacts__item">
        <svg class="contacts__icon" viewBox="0 0 24 24" aria-hidden="true">
          <rect x="6" y="2" width="12" height="20" rx="2" fill="none" stroke="#1e8fd8" stroke-width="2"/>
          <circle cx="12" cy="18" r="1.2" fill="#1e8fd8"/>
        </svg>
        0431 586 207
      </li>
      <li class="contacts__item">
        <svg class="contacts__icon" viewBox="0 0 24 24" aria-hidden="true">
          <rect x="2" y="5" width="20" height="14" fill="#1e8fd8"/>
          <path d="M2 5l10 8 10-8" fill="none" stroke="#161719" stroke-width="1.6"/>
        </svg>
        <span class="contacts__email">gavin@careerlantern.com.au</span>
      </li>
    </ul>
  </section>

  <section class="card card--back" aria-label="Business card back">
    <div class="brand brand--large">
      <span class="brand__square"></span>
      <span class="brand__name">Darrow Consulting</span>
    </div>
  </section>

</main>
</body>
</html>
```